Cybersecurity Start-Up - Velorix

We need a MS Word Template for everyday documents. This would be leveraged to create reports, marketing materials, internal memos etc.

The document should follow the standard MS Word template format and have an H1,H2,H3, paragraph, Title, bold font, regular font, table etc. All editable with normal MS Word features.

Our logo is also attached. We would like to see the same color scheme used throughout the document. Additional attached is a sample word document that outlines all of the components we would like to see in the template.

Requirements
Must have
• - Submission must meet all standard MS Word Template requirements.
• - Submission should make use of Built in MS Styles so as the user of the template I should be able to create a brand new page and insert an H1 for example and be able to select from the styles drop down the same font/color/style that you have designed for your submission.
• - All sections in the provided document need to be contained in your submission.
• - The table of contents should auto update if I add a new page, heading, section etc.
• - Need to read and understand all of my comments which I have placed in the sample document uploaded to the briefing
Should not have
• no fixed textboxes or image boxes. everything needs to be smoothly editable in MS Word. "Editable" means more than just being able to alter text.

```html
<!DOCTYPE html>
<html lang="en">
<head>
<meta charset="utf-8">
<title>Velorix – Word Template Pages</title>
<link rel="stylesheet" href="https://fonts.googleapis.com/css2?family=Arimo:wght@400;700&display=swap">
<style>
:root{
  --green:#86bc3f;
  --green-light:#dfeccb;
  --orange:#f26522;
  --navy:#0e1830;
  --ink:#2b2b2b;
  --grey:#7d7d7d;
  --crit:#8b1a1a;
  --crit-bg:#f3d4d6;
  --high:#e8231f;
  --med:#f2a900;
  --med-bg:#e6dc66;
  --blue:#3aa0c8;
  --blue-bg:#d4ecf6;
}
*{box-sizing:border-box;margin:0;padding:0}
html,body{width:1200px;height:823px;overflow:hidden}
body{
  font-family:"Arimo",Arial,sans-serif;color:var(--ink);
  background:radial-gradient(ellipse at 50% 45%,#3d3d3d 0%,#262626 55%,#141414 100%);
  position:relative;
}
.page{position:absolute;width:261px;height:345px;background:#fff;box-shadow:0 4px 14px rgba(0,0,0,.55);overflow:hidden}
.content{position:absolute;left:21px;right:21px;top:22px}
.footer-rule{position:absolute;left:21px;bottom:16px;width:177px;height:2.5px;display:flex}
.footer-rule i{display:block;height:100%}
.footer-rule .g1{width:28px;background:#777}
.footer-rule .o1{width:37px;background:var(--orange)}
.footer-rule .g2{flex:1;background:var(--green)}
.footer-url{position:absolute;right:20px;bottom:15px;font-size:3px;color:var(--grey)}
.h1{font-weight:700;font-size:8.5px;color:var(--green);margin-bottom:5px}
.h1.orange{color:var(--orange);font-size:9.5px}
.h2{font-weight:700;font-size:5.6px;color:var(--orange);margin:9px 0 4px 6px}
.h2::before{content:"•";margin-right:5px}
p.body{font-size:3.3px;line-height:1.3;text-align:justify}
table{width:100%;border-collapse:collapse;font-size:3.1px}
td,th{padding:0.4px 2px;text-align:left;vertical-align:top}
.bold{font-weight:700}

/* cover */
.brand{font-weight:700;font-size:20px;color:var(--navy);display:flex;align-items:center;gap:5px;letter-spacing:-.2px}
.brand .mark{width:9px;height:9px;background:var(--orange)}
.cover-title{position:absolute;left:14px;top:82px;font-weight:700;font-size:10.5px;color:var(--green)}
.cover-date{position:absolute;left:14px;top:95px;font-weight:700;font-size:5.5px;color:var(--grey)}
.cover-art{position:absolute;left:0;top:0;width:261px;height:345px}

/* toc */
.toc-row{display:flex;align-items:flex-end;font-size:3.6px;font-weight:700;height:5.4px}
.toc-row .lead{flex:1;border-bottom:.5px dotted #555;margin:0 1px 1px}
.toc-gap{height:3.5px}

/* tables */
.work th{background:var(--green);color:#fff;font-weight:700}
.work td{border:.4px solid var(--green);background:#fff}
.work td:first-child{font-weight:700;width:70px}
.work .tint td{background:var(--green-light)}
.module{margin-bottom:7px}
.module td{border-bottom:.4px solid var(--green);background:var(--green-light);font-weight:700;height:4.5px}
.module tr:first-child td{background:#fff}
.module td:nth-child(2){font-weight:400;width:148px}
.blue th{background:var(--blue);color:#fff}
.blue td{background:var(--blue-bg)}
.sev-label{font-weight:700;font-size:4.4px;margin-top:6px}
.sev-label::after{content:"";display:block;width:13px;height:1px;margin-top:1.2px;background:currentColor}
.findings{width:150px}
.findings th{background:#111;color:#fff}
.findings td{border:.4px solid #999}
.findings td.s{color:#fff;text-align:center;font-weight:700}

/* observations */
.obs{border:.8px solid var(--crit);margin-bottom:18px}
.obs .hd{display:flex;justify-content:space-between;background:var(--crit);color:#fff;font-weight:700;font-size:3.4px;padding:1px 2px}
.obs .row{display:flex;border-top:.6px solid #e3a7ab;background:var(--crit-bg);padding:3px 2px}
.obs .row.white{background:#fff}
.obs .lbl{width:56px;font-weight:700;font-size:3.4px;flex:none}
.obs .txt{flex:1;font-size:3.2px;line-height:1.3;text-align:justify}
.obs ul{margin:2px 0 0 14px;font-size:3.2px}
.obs.medium{border-color:var(--med)}
.obs.medium .hd{background:var(--med)}
.obs.medium .row{background:var(--med-bg);border-top-color:#d5c34c}
.obs.medium .row.white{background:#fff}
.shot{width:118px;height:78px;background:linear-gradient(#e4e4e4,#cfcfcf);border:.5px solid #aaa}
.caption{font-size:2.8px;text-align:center;margin-top:3px;font-weight:700}

/* back */
.back{background:linear-gradient(150deg,#142040 0%,var(--navy) 60%,#0a1226 100%)}
.back .brand{color:#fff;position:absolute;left:95px;top:290px;font-size:19px}
.back .contact{position:absolute;left:0;right:0;top:312px;text-align:center;color:#fff;font-size:3.6px;font-weight:700;line-height:1.5;padding-left:50px}
</style>
</head>
<body>

<!-- Cover -->
<section class="page" style="left:40px;top:48px">
  <svg class="cover-art" role="img" aria-label="Geometric pattern of overlapping translucent cubes in beige, yellow, orange and green" viewBox="0 0 261 345">
    <defs>
      <linearGradient id="coverFill" x1="0" y1="0" x2="0.2" y2="1">
        <stop offset="0" stop-color="#d9d5c4"/>
        <stop offset=".5" stop-color="#eddca4"/>
        <stop offset=".8" stop-color="#f3b347"/>
        <stop offset="1" stop-color="#b8c95a"/>
      </linearGradient>
    </defs>
    <polygon points="261,18 261,345 0,345 0,200 130,120 190,60" fill="url(#coverFill)" opacity=".75"/>
  </svg>
  <div class="brand" style="position:absolute;left:14px;top:22px"><span>Velorix</span><span class="mark"></span></div>
  <div class="cover-title">Training Name Goes here</div>
  <div class="cover-date">DATE: 7<sup style="font-size:3.5px">th</sup> MAY 2018</div>
</section>

<!-- Table of contents -->
<section class="page" style="left:325px;top:48px">
  <div class="content" style="top:22px">
    <div class="h1 orange" style="margin-bottom:9px">Table of Contents</div>
    <div class="toc-row">Training Name<span class="lead"></span>2</div><div class="toc-gap"></div>
    <div class="toc-row">Subject Introduction<span class="lead"></span>4</div><div class="toc-gap"></div>
    <div class="toc-row">Subjects recommended<span class="lead"></span>4</div>
    <div class="toc-row">Professional Outcomes<span class="lead"></span>4</div><div class="toc-gap"></div>
    <div class="toc-row">Training Content<span class="lead"></span>4</div>
    <div class="toc-row">Technical Overview<span class="lead"></span>5</div><div class="toc-gap"></div>
    <div class="toc-row">Severity Ratings<span class="lead"></span>5</div>
    <div class="toc-row">Summary Of Findings<span class="lead"></span>5</div>
    <div class="toc-row">Detailed Observations<span class="lead"></span>6</div><div class="toc-gap"></div>
    <div class="toc-row">Critical Findings<span class="lead"></span>7</div>
    <div class="toc-row">High Findings<span class="lead"></span>8</div>
    <div class="toc-row">Medium Findings<span class="lead"></span>9</div>
    <div class="toc-row">Low Findings<span class="lead"></span>10</div><div class="toc-gap"></div>
    <div class="toc-row">Appendix 01 – Engagement Methodology<span class="lead"></span>11</div>
  </div>
  <div class="footer-rule"><i class="g1"></i><i class="o1"></i><i class="g2"></i></div>
  <div class="footer-url">WWW.VELORIX-SEC.COM</div>
</section>

<!-- Subject introduction -->
<section class="page" style="left:615px;top:48px">
  <div class="content" style="top:27px">
    <div class="h1" style="margin-bottom:3px">Subject Introduction</div>
    <p class="body">This section introduces the training subject, its purpose and the audience it serves. It sets out the scope of the course, the skills that learners should gain and the way progress will be measured. Use this space to give readers a short and clear summary before they move on to the detailed sections below.</p>
    <div class="h2" style="margin-top:13px">Subjects recommended</div>
    <p class="body">List the subjects learners should complete before this course. Keep each entry short so readers can scan the list quickly and plan study time.</p>
    <div class="h2" style="margin-top:12px">Professional Outcomes</div>
    <table class="work">
      <tr><th colspan="2">WORK ROLES TABLE</th></tr>
      <tr><td>Work Role Name</td><td></td></tr>
      <tr><td>Specialty Area</td><td></td></tr>
      <tr><td>CSF Category</td><td></td></tr>
      <tr><td>Work Role Description</td><td></td></tr>
      <tr class="tint"><td>Tasks</td><td>This is task 1<br>This is task 2</td></tr>
      <tr><td>Skills</td><td>This is skill 1<br>This is skill 2</td></tr>
      <tr class="tint"><td>Abilities</td><td>This is ability 1<br>This is ability 2</td></tr>
    </table>
    <div class="h2" style="margin-top:11px">Training Content</div>
    <table class="module">
      <tr><td>Module 1 – Table 2</td><td></td></tr>
      <tr><td>Name</td><td>Week</td></tr><tr><td>Module Description</td><td></td></tr>
      <tr><td>Acquired Competences</td><td></td></tr><tr><td>Deliverables</td><td></td></tr>
      <tr><td>Assessment system</td><td></td></tr>
    </table>
    <table class="module">
      <tr><td>Module 2 – Table 2</td><td></td></tr>
      <tr><td>Name</td><td>Week</td></tr><tr><td>Module Description</td><td></td></tr>
      <tr><td>Acquired Competences</td><td></td></tr><tr><td>Deliverables</td><td></td></tr>
      <tr><td>Assessment system</td><td></td></tr>
    </table>
    <table class="module">
      <tr><td>Module 3 – Table 2</td><td></td></tr>
      <tr><td>Name</td><td>Week</td></tr><tr><td>Module Description</td><td></td></tr>
      <tr><td>Acquired Competences</td><td></td></tr><tr><td>Deliverables</td><td></td></tr>
      <tr><td>Assessment system</td><td></td></tr>
    </table>
  </div>
  <div class="footer-rule"><i class="g1"></i><i class="o1"></i><i class="g2"></i></div>
  <div class="footer-url">WWW.VELORIX-SEC.COM</div>
</section>

<!-- Technical overview -->
<section class="page" style="left:902px;top:48px">
  <div class="content" style="top:18px">
    <div class="h2" style="margin-top:0">Technical Overview</div>
    <p class="body">Give a short technical picture of the environment under review, including key systems, network zones and the controls already in place. Note any limits on testing and the dates when work took place so readers understand the context of each finding in this report.</p>
    <table class="blue" style="margin-top:9px">
      <tr><th colspan="2">Table Two</th></tr>
      <tr><th>Sub heading 2</th><th>Sub heading 2</th></tr>
      <tr><td>• Target 1</td><td>• Target 3</td></tr>
      <tr><td>• Target 2</td><td>• Target 4</td></tr>
    </table>
    <div class="h2" style="margin-top:12px">Severity Ratings</div>
    <div class="sev-label" style="color:var(--crit)">Critical</div>
    <p class="body" style="margin-top:4px">Describe what this rating means for the client, how quickly issues at this level should be fixed and who should own the response.</p>
    <div class="sev-label" style="color:var(--high)">High</div>
    <p class="body" style="margin-top:4px">Describe what this rating means for the client, how quickly issues at this level should be fixed and who should own the response.</p>
    <div class="sev-label" style="color:var(--med)">Medium</div>
    <p class="body" style="margin-top:4px">Describe what this rating means for the client, how quickly issues at this level should be fixed and who should own the response.</p>
    <div class="sev-label" style="color:var(--green)">Low</div>
    <p class="body" style="margin-top:4px">Describe what this rating means for the client, how quickly issues at this level should be fixed and who should own the response.</p>
    <div class="h2" style="margin-top:10px">Summary Of Findings</div>
    <p class="body">The table below lists every finding with its rating. Full details for each item follow in the next section of the report.</p>
    <table class="findings" style="margin-top:5px">
      <tr><th>Finding Name</th><th style="text-align:center">Severity</th></tr>
      <tr><td>Critical Finding Title</td><td class="s" style="background:var(--crit)">Critical</td></tr>
      <tr><td>High Finding Title</td><td class="s" style="background:var(--high)">High</td></tr>
      <tr><td>Medium Finding Title</td><td class="s" style="background:var(--med)">Medium</td></tr>
      <tr><td>Low Finding Title</td><td class="s" style="background:var(--green)">Low</td></tr>
    </table>
  </div>
  <div class="footer-rule"><i class="g1"></i><i class="o1"></i><i class="g2"></i></div>
  <div class="footer-url">WWW.VELORIX-SEC.COM</div>
</section>

<!-- Detailed observations -->
<section class="page" style="left:170px;top:439px">
  <div class="content" style="top:16px;left:21px;right:21px">
    <div class="h2" style="margin:0 0 5px 6px">Detailed Observations</div>
    <div class="obs">
      <div class="hd"><span>Insecure Configurations Identified</span><span>CRITICAL</span></div>
      <div class="row"><div class="lbl">Observation</div><div class="txt">The review found services running with default settings and weak access rules. Several hosts accept old protocols and expose admin panels to the wider network. An attacker on the same segment could use these gaps to gain a foothold and move on to more sensitive systems.</div></div>
      <div class="row white"><div class="lbl">Evidence</div><div class="txt"><div class="shot" role="img" aria-label="Screenshot of a configuration console showing the insecure settings"></div><div class="caption" style="width:118px">Figure #1 – This is a caption for the above screenshot</div></div></div>
      <div class="row"><div class="lbl">Recommendation</div><div class="txt"><b>Apply</b> the hardened baseline to all affected hosts, disable legacy protocols and limit admin access to approved jump servers. Review these settings every quarter.
        <ul><li>Remove unused services from each affected host</li><li>Enable logging and forward events to the central store</li></ul></div></div>
      <div class="row white"><div class="lbl">Assets Affected</div><div class="txt"><ul style="margin:0 0 0 8px"><li>127.0.0.1</li><li>127.0.0.2</li><li>127.0.0.3</li></ul></div></div>
    </div>
    <div class="obs medium">
      <div class="hd"><span>Insecure Configurations Identified</span><span>MEDIUM</span></div>
      <div class="row"><div class="lbl">Observation</div><div class="txt">Some file shares allow read access to all staff accounts. Sensitive project files were found in folders that should be limited to a small group. The risk is lower as access still needs a valid login.</div></div>
    </div>
  </div>
  <div class="footer-rule"><i class="g1"></i><i class="o1"></i><i class="g2"></i></div>
  <div class="footer-url">WWW.VELORIX-SEC.COM</div>
</section>

<!-- Continuation + appendix -->
<section class="page" style="left:489px;top:439px">
  <div class="content" style="top:22px">
    <div class="obs medium" style="margin-bottom:14px">
      <div class="row white" style="border-top:none"><div class="lbl">Evidence</div><div class="txt">Screenshots and command output that confirm the finding are placed here with a short caption beneath each image.</div></div>
      <div class="row"><div class="lbl">Recommendation</div><div class="txt"><b>Limit</b> share access to named groups, move sensitive files to restricted folders and review permissions with each team owner.</div></div>
      <div class="row white"><div class="lbl">Assets Affected</div><div class="txt"><ul style="margin:0 0 0 8px"><li>127.0.0.1</li><li>127.0.0.2</li><li>127.0.0.3</li></ul></div></div>
    </div>
    <div class="h1" style="font-size:8px;margin-bottom:3px">Appendix 01 – Engagement Methodology</div>
    <p class="body">This appendix explains how the engagement was planned and run, including scope, tools, testing windows and the way findings were checked and rated before release.</p>
  </div>
  <div class="footer-rule"><i class="g1"></i><i class="o1"></i><i class="g2"></i></div>
  <div class="footer-url">WWW.VELORIX-SEC.COM</div>
</section>

<!-- Back cover -->
<section class="page back" style="left:808px;top:439px" role="img" aria-label="Dark navy back cover with subtle diagonal texture">
  <div class="brand"><span>Velorix</span><span class="mark"></span></div>
  <div class="contact">+01 5550 10234<br>info@velorix-sec.com | www.velorix-sec.com</div>
</section>

</body>
</html>
```